Postcard Design Project

We are a small printing company specializing in envelope printing.
We market to churches and medical offices.

Industry/Entity Type

It Company

```html
<!DOCTYPE html>
<html lang="en">
<head>
<meta charset="utf-8">
<title>KVR Designs – Envelope Postcard</title>
<link href="https://fonts.googleapis.com/css2?family=Open+Sans:wght@400;700;800&display=swap" rel="stylesheet">
<style>
  :root {
    --page-bg: #e8e8e8;
    --card-bg: #ffffff;
    --brand-blue: #0f9ad2;
    --headline-blue: #1597cf;
    --headline-edge: #0b3b58;
    --ink: #1f1f1f;
    --brand-red: #d32027;
    --hero-light: #f3f3f3;
    --hero-mid: #d9d9d9;
    --white: #ffffff;
  }
  * { box-sizing: border-box; margin: 0; padding: 0; }
  html, body { width: 970px; height: 1200px; overflow: hidden; }
  body {
    background: var(--page-bg);
    font-family: "Open Sans", Arial, sans-serif;
    color: var(--ink);
    position: relative;
  }
  .postcard {
    position: absolute;
    left: 82px;
    width: 806px;
    height: 536px;
    background: var(--card-bg);
    overflow: hidden;
  }
  .postcard--front { top: 49px; }
  .postcard--back { top: 612px; }

  .hero-backdrop {
    position: absolute;
    inset: 0 0 109px 0;
    background: radial-gradient(ellipse at 50% 45%, var(--hero-light) 0%, var(--hero-mid) 100%);
  }
  .headline {
    position: absolute;
    top: 36px;
    left: 0;
    width: 806px;
    text-align: center;
    font-weight: 800;
    font-size: 61px;
    line-height: 60px;
    letter-spacing: -2.5px;
    color: var(--headline-blue);
    text-shadow: 2px 2px 0 var(--headline-edge), 0 0 1px var(--headline-edge);
    text-transform: uppercase;
  }
  .subhead {
    position: absolute;
    top: 237px;
    left: 160px;
    width: 580px;
    text-align: center;
    font-weight: 800;
    font-size: 27px;
    line-height: 32px;
    letter-spacing: 0.3px;
    color: var(--ink);
    text-transform: uppercase;
  }
  .service-list {
    position: absolute;
    top: 318px;
    left: 0;
    width: 806px;
    list-style: none;
    font-size: 20.5px;
    line-height: 27px;
    color: var(--ink);
    text-align: center;
  }
  .service-list li { display: block; }
  .service {
    display: inline-block;
    margin: 0 5px;
  }
  .service::before {
    content: "";
    display: inline-block;
    width: 13px;
    height: 13px;
    border: 3px solid var(--brand-blue);
    margin-right: 6px;
    vertical-align: 1px;
  }

  .contact-band {
    position: absolute;
    left: 0;
    bottom: 0;
    width: 806px;
    height: 109px;
    background: var(--brand-blue);
    color: var(--white);
  }
  .contact-text {
    position: absolute;
    left: 20px;
    top: 25px;
    width: 500px;
    text-align: center;
    font-size: 24.5px;
    line-height: 32px;
  }
  .contact-text strong { font-weight: 700; }
  .brand-name {
    position: absolute;
    left: 544px;
    top: 30px;
    width: 230px;
    height: 52px;
    display: flex;
    align-items: center;
    justify-content: center;
    font-weight: 800;
    font-size: 34px;
    letter-spacing: 0.5px;
    color: var(--ink);
    text-transform: uppercase;
  }

  .back-message {
    position: absolute;
    top: 30px;
    left: 18px;
    width: 400px;
    text-align: center;
    font-weight: 800;
    font-size: 32px;
    line-height: 33px;
    letter-spacing: -0.5px;
    color: var(--ink);
    text-transform: uppercase;
  }
  .back-message .accent { color: var(--brand-red); }
  .back-divider {
    position: absolute;
    left: 438px;
    top: 39px;
    width: 2px;
    height: 352px;
    background: #555555;
  }
  .stamp-box {
    position: absolute;
    left: 672px;
    top: 18px;
    width: 119px;
    height: 146px;
    border: 1.5px solid #333333;
  }
  .address-lines {
    position: absolute;
    left: 469px;
    top: 232px;
    width: 290px;
    height: 140px;
  }
</style>
</head>
<body>

  <section class="postcard postcard--front" aria-label="Postcard front">
    <div class="hero-backdrop" role="img" aria-label="Photo of scattered white envelopes with a few colourful green, purple, yellow and blue envelopes"></div>
    <h1 class="headline">Down to your last<br>box of envelopes?<br>No problem.</h1>
    <p class="subhead">Call KVR Designs for fast,<br>economical, quality envelopes.</p>
    <ul class="service-list">
      <li><span class="service">Custom Business Envelopes</span><span class="service">Free Copy Changes</span></li>
      <li><span class="service">Church Offering Envelopes</span><span class="service">Variety of Paper and Size Options</span></li>
      <li><span class="service">Medical Billing Envelopes</span><span class="service">Free Shipping</span></li>
    </ul>
    <footer class="contact-band">
      <p class="contact-text">Call for a free estimate <strong>555-210-4478</strong> or<br>E-mail <strong>orders@kvrprint.com</strong></p>
      <div class="brand-name">KVR Designs</div>
    </footer>
  </section>

  <section class="postcard postcard--back" aria-label="Postcard back">
    <h2 class="back-message">Call <span class="accent">KVR Designs</span> for<br>fast, economical,<br>quality envelopes.</h2>
    <div class="back-divider"></div>
    <div class="stamp-box"></div>
    <svg class="address-lines" viewBox="0 0 290 140" aria-hidden="true">
      <g stroke="#222222" stroke-width="1.5">
        <line x1="0" y1="1" x2="290" y2="1"/>
        <line x1="0" y1="46" x2="290" y2="46"/>
        <line x1="0" y1="91" x2="290" y2="91"/>
        <line x1="0" y1="137" x2="290" y2="137"/>
      </g>
    </svg>
    <footer class="contact-band">
      <p class="contact-text">Call for a free estimate <strong>555-210-4478</strong> or<br>E-mail <strong>orders@kvrprint.com</strong></p>
      <div class="brand-name">KVR Designs</div>
    </footer>
  </section>

</body>
</html>
```